lab equipment website

We need a fresh new look for a company website called tarvio. We will be using the current logo and brand colors on their current website tarvio.com. They want to keep their text and on-page SEO, but would like to reformat it to look more modern and fresh. They want to have everything be high performance with a great user experience. Their main call to action is for people to fill in a contact form so they can call them. There is some information that is purposely above the fold on the instrument pages. I will need the home page, about page and a leasing page.

```html
<!DOCTYPE html>
<html lang="en">
<head>
<meta charset="utf-8">
<title>tarvio — Lab Equipment Leasing</title>
<link rel="stylesheet" href="https://fonts.googleapis.com/css2?family=Open+Sans:wght@400;600;700&family=Roboto:wght@400;500;700&display=swap">
<style>
:root{
  --teal:#17b79a;
  --teal-dark:#0e6b6d;
  --teal-deep:#0b5557;
  --ink:#2d3236;
  --text:#4a4f55;
  --footer:#353b43;
  --footer-line:#4a515a;
  --white:#ffffff;
  --field:#f1f2f3;
}
*{box-sizing:border-box;margin:0;padding:0}
html,body{width:1200px;height:3956px;overflow:hidden}
body{position:relative;font-family:"Open Sans",Arial,sans-serif;color:var(--text);background:var(--white)}
.abs{position:absolute}
h1,h2,h3{font-family:"Roboto",Arial,sans-serif;color:var(--ink)}
p{font-size:13px;line-height:1.55}

/* header */
.site-header{left:0;top:0;width:1200px;height:100px;background:rgba(50,56,64,.88);z-index:2}
.brand{left:120px;top:18px;display:flex;align-items:center;gap:10px}
.brand-mark{width:28px;height:28px;background:var(--teal)}
.brand-name{font-family:"Roboto",sans-serif;font-weight:700;font-size:34px;color:var(--white)}
.topbar{right:118px;top:14px;display:flex;gap:26px;font-size:13px;color:var(--white)}
.topbar span{display:flex;align-items:center;gap:7px}
.topbar .phone{color:var(--teal)}
.ico-circle{width:20px;height:20px;border-radius:50%;background:var(--white);display:inline-flex;align-items:center;justify-content:center}
.main-nav{right:118px;top:52px;display:flex;gap:34px;font-family:"Roboto",sans-serif;font-size:14px;font-weight:500;color:var(--white)}
.main-nav a{color:inherit;text-decoration:none;padding-bottom:14px}
.main-nav a.active{color:var(--teal);border-bottom:3px solid var(--teal)}

/* hero */
.hero{left:0;top:0;width:1200px;height:672px;background:linear-gradient(110deg,#6f747a 0%,#a9adb1 35%,#8b9095 60%,#4e545a 100%)}
.hero-title{left:0;width:1200px;top:328px;text-align:center;color:var(--white);font-size:32px;font-weight:700}
.hero-sub{left:0;width:1200px;top:372px;text-align:center;color:var(--white);font-size:14px}

.btn{display:flex;align-items:center;height:42px}
.btn-hex{width:48px;height:42px;position:relative;z-index:1}
.btn-pill{margin-left:-20px;height:38px;width:210px;border-radius:19px;background:var(--teal);color:var(--white);font-size:13px;font-weight:600;display:flex;align-items:center;justify-content:center;padding-left:20px}

.features{left:0;top:540px;width:1200px;height:250px}
.feature{position:absolute;top:0;width:277px;height:250px}
.feature svg.hex{position:absolute;left:0;top:0}
.feature-body{position:absolute;left:0;top:0;width:277px;height:250px;display:flex;flex-direction:column;align-items:center;padding-top:48px;color:var(--white);text-align:center}
.feature-body p{font-size:16px;line-height:1.35;margin-top:14px;width:210px}
.feature-body .go{margin-top:auto;margin-bottom:36px}

/* about */
.about-title{left:118px;top:878px;font-size:32px;font-weight:700}
.about-text{left:118px;top:952px;width:488px}
.about-text p{margin-bottom:14px}
.about-art{left:628px;top:838px;width:492px;height:349px;background:radial-gradient(circle at 45% 60%,#e6f5ee 0%,#ffffff 70%)}

/* instruments */
.instruments{left:0;top:1279px;width:1200px;height:541px;background:var(--teal-dark)}
.instr-title{left:118px;top:1364px;font-size:30px;font-weight:700;color:var(--white)}
.instr-text{left:118px;top:1471px;width:455px;color:var(--white)}
.instr-text p{margin-bottom:14px}
.instr-art{left:598px;top:1366px;width:478px;height:367px;background:linear-gradient(135deg,#ffffff,#e4e7ea 55%,#ffffff)}

/* trusted */
.trusted-title{left:0;width:1200px;top:1882px;text-align:center;font-size:32px;line-height:40px;font-weight:700;letter-spacing:1.5px}
.trusted-art{left:118px;top:2030px;width:422px;height:238px;background:linear-gradient(160deg,#e8eaec 0%,#c9ced3 50%,#2c4fa3 52%,#2a48a0 60%,#dfe2e5 62%)}
.trusted-text{left:614px;top:2040px;width:506px}
.trusted-text p{margin-bottom:14px}

/* faq */
.faq{left:0;top:2347px;width:1200px;height:553px;background:linear-gradient(120deg,#2f6d72 0%,#3c8086 40%,#2b6167 100%)}
.faq-title{left:121px;top:2452px;font-size:32px;font-weight:700;color:var(--white)}
.faq-list{left:121px;top:2512px;width:525px;list-style:none}
.faq-list li{height:34px;margin-bottom:12px;background:var(--white);display:flex;align-items:center;justify-content:space-between;padding:0 16px;font-size:12px;color:var(--text)}
.consult{left:701px;top:2431px;width:333px;height:385px;background:var(--white);padding:18px 30px}
.consult h3{text-align:center;font-size:17px;font-weight:700;margin-bottom:14px}
.field{height:34px;border:1px solid #9aa0a5;margin-bottom:10px;font-size:12px;padding:8px 10px;color:var(--ink)}
.field.msg{height:112px}
.submit{height:34px;border-radius:17px;background:var(--teal);color:var(--white);font-size:13px;text-align:center;line-height:34px;margin-top:4px}

/* team */
.team-title{left:0;width:1200px;top:2944px;text-align:center;font-size:32px;font-weight:500}
.member{position:absolute;top:3006px;width:193px;text-align:center}
.member .photo{width:193px;height:172px;clip-path:polygon(25% 0,75% 0,100% 50%,75% 100%,25% 100%,0 50%);background:linear-gradient(180deg,#d9dcdf,#9aa1a8)}
.member h3{margin-top:20px;font-size:17px;font-weight:700;letter-spacing:.5px}
.member .role{font-size:13px;margin-top:4px}
.member .social{display:flex;justify-content:center;gap:6px;margin-top:18px}
.dot{width:24px;height:24px;border-radius:50%;background:var(--ink)}
.pager{left:588px;top:3346px;display:flex;gap:8px}
.pager span{width:8px;height:8px;border-radius:50%;background:var(--teal-dark)}
.pager span+span{background:var(--teal)}

/* newsletter */
.news-title{left:0;width:1200px;top:3406px;text-align:center;font-size:26px;font-weight:700}
.news-sub{left:0;width:1200px;top:3446px;text-align:center;font-size:14px}
.news-form{left:272px;top:3489px;width:651px;height:36px;display:flex}
.news-form .input{flex:1;background:var(--field);border-radius:18px 0 0 18px;font-size:13px;padding:9px 24px;color:#8a9096}
.news-form .go{width:128px;background:var(--teal);border-radius:18px;margin-left:-18px;color:var(--white);font-size:14px;font-weight:600;text-align:center;line-height:36px}

/* footer */
.site-footer{left:0;top:3587px;width:1200px;height:321px;background:var(--footer);color:var(--white)}
.f-brand{left:121px;top:3655px;display:flex;align-items:center;gap:10px}
.f-about{left:121px;top:3720px;width:200px;font-size:13px;line-height:1.4;color:var(--white)}
.f-col h4{font-family:"Roboto",sans-serif;font-size:14px;font-weight:500;margin-bottom:28px}
.f-col ul{list-style:none;font-size:13px;line-height:21px}
.f-col ul li::before{content:"";display:inline-block;width:5px;height:5px;border-radius:50%;background:var(--white);margin-right:10px;vertical-align:middle}
.f-contact{font-size:13px;line-height:24px}
.f-contact td{vertical-align:top;padding-right:18px}
.qc{display:grid;grid-template-columns:1fr 1fr;gap:8px;width:274px}
.qc div{height:28px;background:var(--footer-line);font-size:12px;padding:6px 10px}
.qc .wide{grid-column:1/3;height:58px}
.qc .send{grid-column:1/3;width:190px;height:26px;background:var(--teal);text-align:center;line-height:26px;padding:0}
.copyright{left:121px;top:3920px;font-size:13px;color:var(--ink)}
.f-social{right:120px;top:3918px;display:flex;gap:8px}
.f-social span{width:20px;height:20px;border-radius:50%;background:var(--teal)}
.f-social span:nth-child(even){background:var(--teal-dark)}
</style>
</head>
<body>

<div class="abs hero" role="img" aria-label="Laboratory photograph of a row of microscopes on a bench"></div>

<header class="abs site-header">
  <div class="abs brand"><span class="brand-mark"></span><span class="brand-name">tarvio</span></div>
  <div class="abs topbar">
    <span><i class="ico-circle"><svg width="12" height="9" viewBox="0 0 12 9"><rect x=".5" y=".5" width="11" height="8" fill="none" stroke="#353b43"/><path d="M.5 .5 6 5l5.5-4.5" fill="none" stroke="#353b43"/></svg></i>info@tarvio.com</span>
    <span class="phone"><i class="ico-circle" style="background:var(--teal)"><svg width="10" height="10" viewBox="0 0 10 10"><path d="M2 1l2 2-1 1.2a6 6 0 0 0 2.8 2.8L7 6l2 2-1.3 1.3C4.5 9 1 5.5.7 2.3z" fill="#fff"/></svg></i>(415) 555-0186</span>
  </div>
  <nav class="abs main-nav">
    <a class="active">Home</a><a>About us</a><a>Leasing</a><a>Testimonials</a><a>Blog</a><a>Contact us</a>
    <a><svg width="14" height="14" viewBox="0 0 14 14"><circle cx="6" cy="6" r="4.5" fill="none" stroke="#fff" stroke-width="2"/><path d="M9.5 9.5 13 13" stroke="#fff" stroke-width="2"/></svg></a>
  </nav>
</header>

<h1 class="abs hero-title">Your Success, Our Support.</h1>
<p class="abs hero-sub">tarvio is fully dedicated to saving you time and money.</p>
<div class="abs btn" style="left:475px;top:415px">
  <svg class="btn-hex" viewBox="0 0 48 42"><polygon points="12,0 36,0 48,21 36,42 12,42 0,21" fill="var(--teal-deep)"/><path d="M30 21H16m6-6-6 6 6 6" stroke="#fff" stroke-width="3" fill="none"/></svg>
  <div class="btn-pill">Read More</div>
</div>

<section class="abs features">
  <div class="feature" style="left:158px">
    <svg class="hex" width="277" height="250" viewBox="0 0 277 250"><polygon points="138,0 277,62 277,188 138,250 0,188 0,62" fill="var(--teal-dark)" stroke="#fff" stroke-width="4"/></svg>
    <div class="feature-body">
      <svg width="40" height="36" viewBox="0 0 40 36"><rect x="2" y="8" width="36" height="26" rx="3" fill="#fff"/><rect x="14" y="2" width="12" height="8" rx="2" fill="none" stroke="#fff" stroke-width="3"/><path d="M20 14v14M13 21h14" stroke="var(--teal-dark)" stroke-width="4"/></svg>
      <p>Worry free lab equipment PM/repair coverage.</p>
      <svg class="go" width="22" height="22" viewBox="0 0 22 22"><circle cx="11" cy="11" r="9.5" fill="none" stroke="#fff" stroke-width="2"/><path d="M9 7l4 4-4 4" stroke="#fff" stroke-width="2" fill="none"/></svg>
    </div>
  </div>
  <div class="feature" style="left:470px">
    <svg class="hex" width="277" height="250" viewBox="0 0 277 250"><polygon points="138,0 277,62 277,188 138,250 0,188 0,62" fill="var(--teal)" stroke="#fff" stroke-width="4"/></svg>
    <div class="feature-body">
      <svg width="40" height="40" viewBox="0 0 40 40"><circle cx="20" cy="20" r="17" fill="none" stroke="#fff" stroke-width="3"/><path d="M20 9v11h9" stroke="#fff" stroke-width="3" fill="none"/></svg>
      <p>Cost-effective lease structures and payment plans.</p>
      <svg class="go" width="22" height="22" viewBox="0 0 22 22"><circle cx="11" cy="11" r="9.5" fill="none" stroke="#fff" stroke-width="2"/><path d="M9 7l4 4-4 4" stroke="#fff" stroke-width="2" fill="none"/></svg>
    </div>
  </div>
  <div class="feature" style="left:773px">
    <svg class="hex" width="277" height="250" viewBox="0 0 277 250"><polygon points="138,0 277,62 277,188 138,250 0,188 0,62" fill="var(--teal-dark)" stroke="#fff" stroke-width="4"/></svg>
    <div class="feature-body">
      <svg width="40" height="40" viewBox="0 0 40 40"><path d="M14 3h12M17 3v12L6 35h28L23 15V3" fill="none" stroke="#fff" stroke-width="3"/><path d="M10 28h20l3 6H7z" fill="#fff"/></svg>
      <p>Knowledge of the laboratory.</p>
      <svg class="go" width="22" height="22" viewBox="0 0 22 22"><circle cx="11" cy="11" r="9.5" fill="none" stroke="#fff" stroke-width="2"/><path d="M9 7l4 4-4 4" stroke="#fff" stroke-width="2" fill="none"/></svg>
    </div>
  </div>
</section>

<h2 class="abs about-title">About Us</h2>
<div class="abs about-text">
  <p>Our mission is to assist laboratories that seek to further scientific innovation. By providing equipment leasing and hassle free repair coverage, we aim to accelerate research and relieve laboratories of heavy financial burdens.</p>
  <p>At the rate that science and technology move, researchers should not be slowed down by inaccessible or unaffordable research equipment.</p>
  <p>Our leasing model stands behind this statement, promising labs financial and operational flexibility</p>
</div>
<div class="abs btn" style="left:118px;top:1140px">
  <svg class="btn-hex" viewBox="0 0 48 42"><polygon points="12,0 36,0 48,21 36,42 12,42 0,21" fill="var(--teal-dark)"/><path d="M30 21H16m6-6-6 6 6 6" stroke="#fff" stroke-width="3" fill="none"/></svg>
  <div class="btn-pill">Read More</div>
</div>
<div class="abs about-art" role="img" aria-label="Illustration of laboratory glassware, flasks, a microscope and a stopwatch"></div>

<section class="abs instruments"></section>
<h2 class="abs instr-title">Instruments &amp; Service</h2>
<div class="abs instr-text">
  <p>So why our laboratory equipment leasing program? Because when capital is limited, purchasing equipment poses a serious burden. Fortunately there is a solution: tarvio. Our laboratory support services allow you to use equipment for a fraction of the price as well as the freedom to utilize different machines for various lengths of time, instead of being tied down to a single machine.</p>
  <p>Plus, when you collaborate with tarvio and anything goes wrong with our machine, we've got your back with our stress-free repair coverage. With tarvio's all-inclusive equipment packages, there is an affordable solution to an expensive problem.</p>
</div>
<div class="abs btn" style="left:118px;top:1688px">
  <svg class="btn-hex" viewBox="0 0 48 42"><polygon points="12,0 36,0 48,21 36,42 12,42 0,21" fill="#fff"/><path d="M30 21H16m6-6-6 6 6 6" stroke="var(--teal-dark)" stroke-width="3" fill="none"/></svg>
  <div class="btn-pill" style="background:#fff;color:var(--teal-dark)">Read More</div>
</div>
<div class="abs instr-art" role="img" aria-label="Photograph of laboratory analysis instruments and a microscope"></div>

<h2 class="abs trusted-title">Trusted Company Offering Scientific<br>Equipment Service Plans and<br>Flexible Leases</h2>
<div class="abs trusted-art" role="img" aria-label="Photograph of a benchtop laboratory analyzer"></div>
<div class="abs trusted-text">
  <p>At tarvio, our goal is to ensure the success of your business. Whether you are running a laboratory or other scientific facilities, we want to keep you provided with the best in cutting-edge equipment.</p>
  <p>That's why we offer flexible scientific equipment leasing options with worry-free service plans– to provide your business with the tools needed to perform at its peak.</p>
</div>
<div class="abs btn" style="left:614px;top:2185px">
  <svg class="btn-hex" viewBox="0 0 48 42"><polygon points="12,0 36,0 48,21 36,42 12,42 0,21" fill="var(--teal-dark)"/><path d="M30 21H16m6-6-6 6 6 6" stroke="#fff" stroke-width="3" fill="none"/></svg>
  <div class="btn-pill">Read More</div>
</div>

<section class="abs faq" role="img" aria-label="Teal-tinted photograph of colleagues in a meeting"></section>
<h2 class="abs faq-title">Frequently Asked Questions</h2>
<ul class="abs faq-list">
  <li>Lorem Ipsum is simply dummy text of the printing.<svg width="10" height="6"><path d="M0 0h10L5 6z" fill="#2d3236"/></svg></li>
  <li>Lorem Ipsum is simply dummy text of the printing.<svg width="10" height="6"><path d="M0 0h10L5 6z" fill="#2d3236"/></svg></li>
  <li>Lorem Ipsum is simply dummy text of the printing.<svg width="10" height="6"><path d="M0 0h10L5 6z" fill="#2d3236"/></svg></li>
  <li>Lorem Ipsum is simply dummy text of the printing.<svg width="10" height="6"><path d="M0 0h10L5 6z" fill="#2d3236"/></svg></li>
  <li>Lorem Ipsum is simply dummy text of the printing.<svg width="10" height="6"><path d="M0 0h10L5 6z" fill="#2d3236"/></svg></li>
  <li>Lorem Ipsum is simply dummy text of the printing.<svg width="10" height="6"><path d="M0 0h10L5 6z" fill="#2d3236"/></svg></li>
  <li>Lorem Ipsum is simply dummy text of the printing.<svg width="10" height="6"><path d="M0 0h10L5 6z" fill="#2d3236"/></svg></li>
</ul>
<form class="abs consult">
  <h3>Free Consultation</h3>
  <div class="field">Name</div>
  <div class="field">Phone</div>
  <div class="field">Email</div>
  <div class="field msg">Message</div>
  <div class="submit">Submit</div>
</form>

<h2 class="abs team-title">Our Team</h2>
<div class="member" style="left:256px">
  <div class="photo" role="img" aria-label="Portrait photograph of team member"></div>
  <h3>LEO MARSH</h3><div class="role">Lab Relations</div>
  <div class="social"><span class="dot"></span><span class="dot"></span><span class="dot"></span></div>
</div>
<div class="member" style="left:540px">
  <div class="photo" role="img" aria-label="Portrait photograph of team member"></div>
  <h3>DANA PRICE</h3><div class="role">Finance</div>
  <div class="social"><span class="dot"></span><span class="dot"></span><span class="dot"></span></div>
</div>
<div class="member" style="left:746px">
  <div class="photo" role="img" aria-label="Portrait photograph of team member"></div>
  <h3>RAVI SETHI</h3><div class="role">Operations</div>
  <div class="social"><span class="dot"></span><span class="dot"></span><span class="dot"></span></div>
</div>
<div class="abs pager"><span></span><span></span></div>

<h2 class="abs news-title">Subscribe To Our Newsletter</h2>
<p class="abs news-sub">To Receive The latest News And Update</p>
<div class="abs news-form"><div class="input">Your E-Mail</div><div class="go">Submit</div></div>

<footer class="abs site-footer"></footer>
<div class="abs f-brand"><span class="brand-mark"></span><span class="brand-name">tarvio</span></div>
<p class="abs f-about">Lorem Ipsum is simply dummy in text of the printing and types ettingin the industry …</p>
<div class="abs f-col" style="left:361px;top:3654px;color:#fff">
  <h4>Quick Link</h4>
  <ul><li>Home</li><li>Services</li><li>Leasing</li><li>Our Team</li><li>About us</li><li>FAQ</li><li>Contact us</li></ul>
</div>
<div class="abs f-col" style="left:485px;top:3654px;color:#fff">
  <h4>Contact us</h4>
  <table class="f-contact">
    <tr><td>Tarvio Inc. :</td><td>240 Harlow Street<br>Suite 410<br>Oakland, CA 94607</td></tr>
    <tr><td>Phone</td><td>: (415) 555-0186</td></tr>
    <tr><td>E-mail</td><td>: info@tarvio.com</td></tr>
  </table>
</div>
<div class="abs f-col" style="left:807px;top:3654px;color:#fff">
  <h4>Quick Contact</h4>
  <div class="qc"><div>Name</div><div>Phone</div><div class="wide">Message</div><div class="send">SEND</div></div>
</div>
<p class="abs copyright">© Copyright 2019 tarvio. All Rights Reserved.</p>
<div class="abs f-social"><span></span><span></span><span></span><span></span><span></span><span></span></div>

</body>
</html>
```